BUSINESS CARD - HALVERDINE RURAL SERVICES

I would like to create a business card for my fertilizer spreading business. I would like to incorporate my existing logo and also a description of the services offered. The business card will be given to farmers so must be kept simple but effective. It will also be left in stores so much also be eye catching in order to stand out from other cards.

Target Market(s)

FARMERS

Requirements
Must have
• FRONT OF CARD = EXISTING LOGO + "CUSTOMISED SPREADING" below the logo

REAR Of CARD = SERVICES OFFERED AND CONTACT DETAILS

- Bulk fertilizer including Lime, Gypsum, Manure & Compost
- Granular fertilizer including Single Super, Urea, Gran-am, & Custom Blends
- Modern equipment - Autosteer & Variable Rate Capable
- Friendly & Reliable Service
- Contact Gus: 0471 502 318
Nice to have
• utilize same color scheme as existing logo

```html
<!DOCTYPE html>
<html lang="en">
<head>
<meta charset="utf-8">
<title>Halverdine Rural Services – Business Card</title>
<link rel="stylesheet" href="https://fonts.googleapis.com/css2?family=Poppins:wght@400;500;700&family=Montserrat:wght@700&display=swap">
<style>
  :root {
    --orange: #f39322;
    --charcoal: #58585b;
    --light-grey: #d9d9d9;
    --white: #ffffff;
    --page: #f1f1f1;
    --text-grey: #4c4c4f;
  }
  * { margin: 0; padding: 0; box-sizing: border-box; }
  html, body { width: 1200px; height: 1200px; overflow: hidden; }
  body {
    background: var(--page);
    font-family: "Poppins", sans-serif;
    position: relative;
  }
  .card {
    position: absolute;
    width: 718px;
    height: 412px;
    overflow: hidden;
  }
  .card--rear { left: 146px; top: 136px; background: var(--white); }
  .card--front { left: 337px; top: 653px; background: var(--charcoal); }

  .rings { position: absolute; inset: 0; }

  .brand {
    position: absolute;
    display: flex;
    flex-direction: column;
    align-items: center;
    text-align: center;
  }
  .brand__dot {
    border-radius: 50%;
    background: var(--orange);
  }
  .brand__name {
    font-family: "Poppins", sans-serif;
    font-weight: 700;
    line-height: 1.05;
    letter-spacing: -0.5px;
  }
  .card--rear .brand { left: 542px; top: 50px; transform: translateX(-50%); }
  .card--rear .brand__dot { width: 84px; height: 84px; margin-bottom: 14px; }
  .card--rear .brand__name { color: var(--charcoal); font-size: 25px; }

  .card--front .brand { left: 359px; top: 86px; transform: translateX(-50%); }
  .card--front .brand__dot { width: 128px; height: 128px; margin-bottom: 18px; }
  .card--front .brand__name { color: var(--white); font-size: 36px; }

  .services {
    position: absolute;
    left: 59px;
    top: 276px;
    list-style: none;
    color: var(--text-grey);
    font-size: 14px;
    font-weight: 500;
    line-height: 16.6px;
  }
  .services li::before { content: "- "; }

  .tagline {
    position: absolute;
    left: 0; right: 0;
    top: 364px;
    text-align: center;
    color: var(--white);
    font-family: "Montserrat", sans-serif;
    font-weight: 700;
    font-size: 21px;
    letter-spacing: 1px;
  }
</style>
</head>
<body>
  <section class="card card--rear" aria-label="Business card, services side">
    <svg class="rings" width="718" height="412" viewBox="0 0 718 412" aria-hidden="true">
      <circle cx="76" cy="84" r="146" fill="var(--charcoal)"/>
      <circle cx="76" cy="84" r="116" fill="var(--orange)"/>
      <circle cx="52" cy="60" r="98" fill="var(--light-grey)"/>
      <circle cx="52" cy="60" r="82" fill="var(--white)"/>
      <circle cx="712" cy="384" r="80" fill="var(--charcoal)"/>
      <circle cx="712" cy="384" r="66" fill="var(--orange)"/>
      <circle cx="722" cy="394" r="58" fill="var(--light-grey)"/>
      <circle cx="722" cy="394" r="48" fill="var(--white)"/>
    </svg>

    <div class="brand">
      <span class="brand__dot" aria-hidden="true"></span>
      <p class="brand__name">Halverdine Rural<br>Services</p>
    </div>

    <ul class="services">
      <li>Bulk fertilizer including Lime, Gypsum, Manure &amp; Composts</li>
      <li>Granular fertilizer including Single Super, Urea, Gran-am, &amp; Custom Blends</li>
      <li>Modern equipment</li>
      <li>Friendly &amp; Reliable Service</li>
      <li>Contact Gus: 0471 502 318</li>
    </ul>
  </section>

  <section class="card card--front" aria-label="Business card, front side">
    <div class="brand">
      <span class="brand__dot" aria-hidden="true"></span>
      <p class="brand__name">Halverdine Rural<br>Services</p>
    </div>
    <p class="tagline">CUSTOMISED SPREADING</p>
  </section>
</body>
</html>
```